Dance Card to Provide Contact Info

I'm looking for a double sided business card to provide contact information to perspective dance partners.
One side of the card would have the words: "Yes I would love to Dance" written in an interesting and eye catching way. Below that would be the three categories I'm interested in
>Social >Exhibition >Competition
The other side of the card would include a picture of me with my Name, Phone Number, and Email Address (Dale Penwick, 210-547-2183, dale@twirlmerry.dance)
My target market is middle aged women interested in Country and Western dancing and West Coast Swing dancing. I am NOT particularly interested in Ballroom style.
Here are a few links to the type of dancing I want to do:
http://www.fpqlx.org/
http://www.prairiestepguildnetwork.com/
http://bexarridgepartnerspin.com/
Business
Contact Information for Business Card
Dale Penwick
210-547-2183
dale@twirlmerry.dance

```html
<!DOCTYPE html>
<html lang="en">
<head>
<meta charset="utf-8">
<title>Dale Penwick – Dance Card</title>
<link href="https://fonts.googleapis.com/css2?family=Jost:wght@300;400;600;700&family=Cinzel:wght@500;700&display=swap" rel="stylesheet">
<style>
  :root {
    --ink-black: #000000;
    --card-orange: #e69a26;
    --headline-grey: #6d6e71;
    --item-grey: #b9b9bb;
    --rule-gold: #a8792a;
    --band-dim: #4f4028;
    --band-bright: #a8832e;
    --shadow-amber: #c0842a;
    --contact-ink: #4a4a4c;
    --rule-dark: #7a5f33;
    --photo-tone: #6a4e3e;
  }
  * { margin: 0; padding: 0; box-sizing: border-box; }
  html, body { width: 1200px; height: 1050px; overflow: hidden; background: var(--ink-black); }
  .card { position: relative; width: 1200px; height: 1050px; }

  .side-invite { position: absolute; left: 0; top: 0; width: 600px; height: 1050px; background: var(--ink-black); overflow: hidden; }
  .headline { font-family: "Jost", sans-serif; color: var(--headline-grey); position: absolute; white-space: nowrap; line-height: 1; }
  .headline-yes { right: 34px; top: 64px; font-size: 70px; font-weight: 300; letter-spacing: -2px; }
  .headline-love { right: 20px; top: 130px; font-size: 106px; font-weight: 300; letter-spacing: -2px; }
  .headline-dance { left: -6px; top: 200px; font-size: 202px; font-weight: 600; letter-spacing: -6px; transform: scaleX(0.92); transform-origin: left top; }

  .interests-rule { position: absolute; left: 60px; width: 540px; height: 1px; background: var(--rule-gold); }
  .interests-rule.top { top: 498px; }
  .interests-rule.bottom { top: 552px; }
  .interests-title { position: absolute; left: 72px; top: 504px; font-family: "Cinzel", serif; font-weight: 500; font-size: 29px; color: var(--item-grey); letter-spacing: 1px; }
  .interest-list { list-style: none; position: absolute; left: 66px; top: 564px; }
  .interest-list li { font-family: "Cinzel", serif; font-weight: 700; font-size: 32px; color: var(--item-grey); height: 66px; letter-spacing: 1px; }
  .interest-list li::before { content: "\2666"; font-size: 22px; vertical-align: 10px; margin-right: 4px; }

  .accent-band { position: absolute; left: 170px; top: 950px; width: 430px; height: 100px;
    background: linear-gradient(90deg, var(--band-dim) 0%, var(--band-dim) 40%, var(--band-bright) 55%, var(--band-dim) 70%, var(--band-dim) 100%); }

  .side-contact { position: absolute; left: 600px; top: 0; width: 600px; height: 1050px; background: var(--card-orange); }
  .portrait-shadow { position: absolute; left: 70px; top: 240px; width: 210px; height: 260px; background: var(--shadow-amber); }
  .portrait { position: absolute; left: 54px; top: 221px; width: 204px; height: 256px; background: linear-gradient(160deg, #7a5a48 0%, var(--photo-tone) 55%, #1c1a1a 100%); }
  .contact-name { position: absolute; left: 56px; top: 528px; font-family: "Jost", sans-serif; font-weight: 600; font-size: 42px; color: var(--contact-ink); white-space: nowrap; transform: scaleX(0.8); transform-origin: left top; }
  .contact-email { position: absolute; left: 54px; top: 582px; font-family: "Jost", sans-serif; font-weight: 300; font-size: 35px; color: var(--contact-ink); white-space: nowrap; }
  .contact-rule { position: absolute; left: 46px; width: 520px; height: 1px; background: var(--rule-dark); }
  .contact-rule.top { top: 680px; }
  .contact-rule.bottom { top: 794px; }
  .contact-phone { position: absolute; left: 46px; top: 672px; font-family: "Jost", sans-serif; font-weight: 300; font-size: 85px; color: var(--contact-ink); white-space: nowrap; }
</style>
</head>
<body>
<div class="card">
  <section class="side-invite">
    <div class="headline headline-yes">YES I WOULD</div>
    <div class="headline headline-love">LOVE TO</div>
    <div class="headline headline-dance">DANCE</div>

    <div class="interests-rule top"></div>
    <div class="interests-title">I'm interested in</div>
    <div class="interests-rule bottom"></div>
    <ul class="interest-list">
      <li>Social</li>
      <li>Exhibition</li>
      <li>Competition</li>
    </ul>

    <div class="accent-band" role="img" aria-label="Decorative band of gold chevrons pointing right"></div>
  </section>

  <section class="side-contact">
    <div class="portrait-shadow"></div>
    <div class="portrait" role="img" aria-label="Portrait photo of Dale Penwick"></div>
    <div class="contact-name">DALE PENWICK</div>
    <div class="contact-email">dale@twirlmerry.dance</div>
    <div class="contact-rule top"></div>
    <div class="contact-phone">210-547-2183</div>
    <div class="contact-rule bottom"></div>
  </section>
</div>
</body>
</html>
```